A portal to our hosted desktop

Looking for a web portal into our hosted desktop. It will be accessible via http://www.qelvoris.com.au/pages/portal which is not created yet.

We are happy for the designs to link in with the current website design but also happy to accept designs that do not. We would like the website to have the following buttons:

• Login
• Speed Test
• Log Support Request
• Resources

We would like a system notification area that we can display messages on.

We also like the idea of a traffic light system (Green, Orange, Red). Green, meaning all systems are a go. Orange meaning maintenance is occurring and red meaning the system is down.

Target Market(s)

Web Developers and Graphic Designers

Coding

Coded - Design and coding required

Number of Pages Required

1 page

Requirements
Must have
• Buttons for the following:
• Login
• Speed Test
• Log Support Request
• Resources
• Notification area and color system to know if everything is a-o-k

```html
<!DOCTYPE html>
<html lang="en">
<head>
<meta charset="utf-8">
<title>Qelvoris Hosted Desktop Portal</title>
<link href="https://fonts.googleapis.com/css2?family=Open+Sans:wght@400;600;700&display=swap" rel="stylesheet">
<style>
  :root {
    --brand-blue: #1f9ad6;
    --nav-text: #111111;
    --white: #ffffff;
    --footer-text: #333333;
    --band: rgba(6, 22, 34, 0.86);
    --green: #1e9a22;
    --orange: #ff6a0a;
    --red: #c40a0a;
    --social: #3a6fb5;
  }
  * { box-sizing: border-box; margin: 0; padding: 0; }
  html, body { width: 1200px; height: 837px; overflow: hidden; background: var(--white); }
  body { font-family: "Open Sans", sans-serif; position: relative; }

  .site-header { position: absolute; left: 0; top: 0; width: 1200px; height: 93px; }
  .brand { position: absolute; left: 111px; top: 14px; height: 66px; display: flex; align-items: center; gap: 10px; }
  .brand-mark { width: 66px; height: 66px; border-radius: 50%; background: var(--brand-blue); }
  .brand-name { font-size: 34px; font-weight: 700; color: var(--brand-blue); line-height: 1; letter-spacing: 1px; }

  .main-nav { position: absolute; top: 32px; right: 110px; display: flex; align-items: center; }
  .main-nav a { font-size: 12px; font-weight: 700; color: var(--nav-text); text-decoration: none; text-transform: uppercase; }
  .nav-speed { margin-right: 40px; }
  .nav-support { margin-right: 28px; }
  .nav-resources { margin-right: 12px; }
  .main-nav .nav-login { background: var(--brand-blue); color: var(--white); width: 96px; height: 30px; display: flex; align-items: center; justify-content: center; font-weight: 600; font-size: 12.5px; }

  .hero { position: absolute; left: 0; top: 93px; width: 1200px; height: 672px; }
  .hero-photo { position: absolute; inset: 0;
    background: radial-gradient(ellipse at 85% 20%, #c8b8a8 0%, rgba(120,140,160,0) 35%),
                linear-gradient(90deg, #3d5f7a 0%, #2a3f58 30%, #1d2a40 50%, #2a3f58 70%, #5a7890 100%); }
  .hero-title { position: absolute; left: 0; width: 1200px; top: 293px; text-align: center; color: var(--white); font-size: 30px; font-weight: 600; line-height: 43px; }
  .hero-title .accent { color: var(--brand-blue); }
  .slide-arrow { position: absolute; top: 280px; width: 16px; height: 24px; }
  .slide-prev { left: 85px; }
  .slide-next { left: 1100px; }

  .notifications { position: absolute; left: 0; top: 541px; width: 1200px; height: 131px; background: var(--band); }
  .notifications h2 { text-align: center; color: var(--brand-blue); font-size: 22px; font-weight: 400; margin-top: 14px; }
  .status { position: absolute; top: 65px; display: flex; align-items: center; }
  .status-light { width: 38px; height: 38px; border-radius: 50%; border: 2px solid #e8e8e8; margin-right: 8px; }
  .status-green { left: 137px; }
  .status-orange { left: 447px; }
  .status-red { left: 779px; }
  .status-green .status-light { background: radial-gradient(circle at 40% 35%, #3fc040, var(--green) 60%, #0c5e10); }
  .status-orange .status-light { background: radial-gradient(circle at 40% 35%, #ffa040, var(--orange) 60%, #c03a00); }
  .status-red .status-light { background: radial-gradient(circle at 40% 35%, #e83030, var(--red) 60%, #700000); }
  .status-label { color: var(--white); font-size: 12.5px; font-weight: 700; line-height: 1.4; }
  .status-desc { color: var(--white); font-size: 13px; line-height: 1.4; }

  .site-footer { position: absolute; left: 0; top: 765px; width: 1200px; height: 72px; }
  .copyright { position: absolute; left: 111px; top: 28px; font-size: 12.5px; color: var(--footer-text); }
  .social { position: absolute; left: 1006px; top: 25px; display: flex; gap: 5px; }
  .social a { width: 24px; height: 24px; border-radius: 50%; background: var(--social); display: block; }
  .social a.social-feed { background: #f08a24; }
</style>
</head>
<body>
  <header class="site-header">
    <div class="brand">
      <div class="brand-mark"></div>
      <span class="brand-name">QELVORIS</span>
    </div>
    <nav class="main-nav">
      <a class="nav-speed" href="#">Speed Test</a>
      <a class="nav-support" href="#">Log Support Request</a>
      <a class="nav-resources" href="#">Resources</a>
      <a class="nav-login" href="#">Login</a>
    </nav>
  </header>

  <section class="hero">
    <div class="hero-photo" role="img" aria-label="Businessman in a dark suit leaning over a glowing desk in front of a city skyline window"></div>
    <svg class="slide-arrow slide-prev" viewBox="0 0 16 24" aria-hidden="true"><path d="M12 3 L4 12 L12 21" fill="none" stroke="#fff" stroke-width="3"/></svg>
    <svg class="slide-arrow slide-next" viewBox="0 0 16 24" aria-hidden="true"><path d="M4 3 L12 12 L4 21" fill="none" stroke="#fff" stroke-width="3"/></svg>
    <h1 class="hero-title"><span class="accent">QELVORIS</span> is an Information Technology support<br>and solutions service provider</h1>

    <div class="notifications">
      <h2>System Notification</h2>
      <div class="status status-green">
        <span class="status-light"></span>
        <div><div class="status-label">GREEN</div><div class="status-desc">Green, meaning all systems are a go</div></div>
      </div>
      <div class="status status-orange">
        <span class="status-light"></span>
        <div><div class="status-label">ORANGE</div><div class="status-desc">Orange meaning maintenance is occurring</div></div>
      </div>
      <div class="status status-red">
        <span class="status-light"></span>
        <div><div class="status-label">RED</div><div class="status-desc">Red meaning the system is down</div></div>
      </div>
    </div>
  </section>

  <footer class="site-footer">
    <p class="copyright">© 2015 Company Name,All The Rights Reserved</p>
    <div class="social">
      <a href="#" aria-label="Social profile"></a>
      <a href="#" aria-label="Professional network"></a>
      <a href="#" class="social-feed" aria-label="News feed"></a>
    </div>
  </footer>
</body>
</html>
```